Business Card

I need a business card that really pops for a potential customer or person who refers a personal injury lead. I want to highlight our office locations, but only address that needs to be on the card is my office's main address. I want a sleek, modern and minimalist design.

```html
<!DOCTYPE html>
<html lang="en">
<head>
<meta charset="utf-8">
<title>Northfield Injury Lawyers – Business Card</title>
<link href="https://fonts.googleapis.com/css2?family=Jost:wght@300;400;500&display=swap" rel="stylesheet">
<style>
  :root {
    --bg: #2e2e2e;
    --card-dark: #262626;
    --band: #333333;
    --emboss: #3d3d3d;
    --white: #ffffff;
    --ink: #2b2b2b;
    --ink-soft: #555555;
    --rule: #bdbdbd;
  }
  * { margin: 0; padding: 0; box-sizing: border-box; }
  html, body { width: 1200px; height: 689px; overflow: hidden; }
  body {
    background: var(--bg);
    font-family: "Jost", sans-serif;
    position: relative;
  }
  .card {
    position: absolute;
    width: 500px;
    height: 286px;
    border-radius: 16px;
    overflow: hidden;
    top: 201px;
  }
  .card--back { left: 70px; background: var(--card-dark); }
  .card--front { left: 630px; background: var(--white); }

  .firm-name {
    position: absolute;
    left: 0; right: 0;
    text-align: center;
    font-size: 28px;
    font-weight: 400;
    letter-spacing: 0;
    line-height: 1;
  }
  .card--back .firm-name { top: 129px; color: var(--emboss); }

  .front-band {
    position: absolute;
    left: 0; top: 0;
    width: 100%;
    height: 150px;
    background: var(--band);
  }
  .card--front .firm-name { top: 61px; color: var(--white); }

  .details {
    position: absolute;
    top: 150px; left: 0; right: 0; bottom: 0;
    display: flex;
    align-items: center;
    justify-content: center;
    gap: 18px;
  }
  .person { text-align: right; color: var(--ink); }
  .person__name { font-size: 20px; font-weight: 500; letter-spacing: 0.5px; line-height: 1.1; }
  .person__title { font-size: 12px; color: var(--ink-soft); margin-bottom: 6px; }
  .person__address { font-size: 12.5px; line-height: 1.35; color: var(--ink-soft); font-weight: 300; }
  .divider { width: 1px; height: 86px; background: var(--rule); }
  .contacts { list-style: none; font-size: 11.5px; color: var(--ink-soft); font-weight: 300; }
  .contacts li { display: flex; align-items: center; gap: 8px; line-height: 1.55; }
  .contacts svg { width: 10px; height: 10px; fill: var(--ink); flex: none; }
</style>
</head>
<body>

<section class="card card--back" aria-label="Card back">
  <p class="firm-name">Northfield Injury Lawyers</p>
</section>

<section class="card card--front" aria-label="Card front">
  <div class="front-band"></div>
  <p class="firm-name">Northfield Injury Lawyers</p>
  <div class="details">
    <div class="person">
      <p class="person__name">DANIEL REYES</p>
      <p class="person__title">President</p>
      <p class="person__address">280 West Lake Avenue<br>Suite 1800, Chicago, IL 60611</p>
    </div>
    <div class="divider"></div>
    <ul class="contacts">
      <li><svg viewBox="0 0 10 10"><path d="M2 0.5l1.6 0 .6 2.4-1.1.8a5.5 5.5 0 0 0 2.7 2.7l.8-1.1 2.4.6 0 1.6c0 .8-.7 1.5-1.5 1.5A8 8 0 0 1 .5 2C.5 1.2 1.2.5 2 .5z"/></svg>312-555-0147</li>
      <li><svg viewBox="0 0 10 10"><path d="M2.5 0h5a.8.8 0 0 1 .8.8v8.4a.8.8 0 0 1-.8.8h-5a.8.8 0 0 1-.8-.8V.8A.8.8 0 0 1 2.5 0zm.4 1.2v6.6h4.2V1.2z"/></svg>312-555-0193</li>
      <li><svg viewBox="0 0 10 10"><path d="M0 2h10v6H0zM.8 2.6 5 5.6l4.2-3z" fill-rule="evenodd"/></svg>info@northfieldinjurylawyers.com</li>
      <li><svg viewBox="0 0 10 10"><circle cx="5" cy="5" r="4.6"/></svg>northfieldinjurylawyers.com</li>
    </ul>
  </div>
</section>

</body>
</html>
```